OLU58 biz card & Stationery

LU58 is a personalized shopping experience brought to you, that lets you find and discover fashion goods through a collection of boutiques curated by taste-makers - celebrities, stylists, designers, and fashion bloggers. Boutiques uses visual technology to help fashionistas discover and shop their look and creates the opportunity for designers to showcase their collections and latest inspirations online.

OLU58 is built on technology developed by our team of fashion experts who work with engineers to “teach” our computer systems to understand various patterns, pairings, and genre definitions. When signed into your account, OLU58 learns about your style and preferences and in turn, provides you better results and recommendations over time. Ultimately, OLU58 will provide shoppers with a much richer and interactive shopping experience and help drive traffic to retailers' websites.

We need a definitely cool business card. The card must be black! And must use our official logo which can be download from OLU58.com

The address for Letter head and evenlop, please use 4872 Crestwick Parkway, Sutie 510 Los Angeles CA90412, email will be anyone@OLU58.com, website is www.OLU58.com

thanks

We received some of the design, thanks. But most of the design are not what we want. We need a very clean version with black ground, you may also use some dark gray to add the element. please take a look at http://morvalstudio.no/work/#pelter__ostrama/, we do like this kind of design very much. hope it help.

```html
<!DOCTYPE html>
<html lang="en">
<head>
<meta charset="utf-8">
<title>OLU58 Business Card</title>
<link rel="stylesheet" href="https://fonts.googleapis.com/css2?family=Tenor+Sans&display=swap">
<style>
  :root {
    --backdrop: #6f6d6d;
    --card: #000000;
    --ink: #ffffff;
  }
  html, body {
    margin: 0;
    padding: 0;
    width: 1200px;
    height: 900px;
    overflow: hidden;
    background: var(--backdrop);
  }
  .canvas {
    position: relative;
    width: 1200px;
    height: 900px;
    font-family: "Tenor Sans", "Optima", sans-serif;
    color: var(--ink);
  }
  .card {
    position: absolute;
    width: 328px;
    height: 537px;
    background: var(--card);
  }
  .card--front { left: 252px; top: 165px; }
  .card--back  { left: 620px; top: 195px; }

  .holder {
    position: absolute;
    left: 28px;
    top: 20px;
  }
  .holder__name {
    margin: 0;
    font-size: 36px;
    font-weight: 400;
    line-height: 1.1;
  }
  .holder__role {
    margin: 2px 0 0;
    font-size: 20px;
    line-height: 1.2;
  }
  .contact {
    position: absolute;
    right: 28px;
    bottom: 24px;
    margin: 0;
    font-style: normal;
    text-align: right;
    font-size: 15px;
    line-height: 20px;
  }

  .brand {
    position: absolute;
    left: 0;
    right: 0;
    top: 50%;
    transform: translateY(-50%);
    margin: 0;
    text-align: center;
    font-size: 36px;
    font-weight: 400;
    line-height: 1;
    white-space: nowrap;
  }
</style>
</head>
<body>
  <main class="canvas">
    <section class="card card--front">
      <div class="holder">
        <h1 class="holder__name">Your Name</h1>
        <p class="holder__role">creative director</p>
      </div>
      <address class="contact">
        4872 Crestwick Parkway,<br>
        Suite 510 Los Angeles Ca90412<br>
        Mobile 000-0000<br>
        anyone@OLU58.com<br>
        www.OLU58.com
      </address>
    </section>

    <section class="card card--back">
      <p class="brand">OLU58</p>
    </section>
  </main>
</body>
</html>
```